Business Card: RW Office Partners - Your organised problem solver

Business Name: RW Office Partners
Website: www.rwofficepartners-example.com.au
Email: maribel@rwofficepartners-example.com.au
Mobile: 61 400 000 000
Facebook: @rwofficepartners
Instrgram: @rwofficepartners

Brading Colours:
HEX
#986474
#ddccd3
#7a8498
#c9d8e4
#000000
#ffffff

Tag Line: Your organised problem solver

Link to DRAFT website:
https://draftsites-example.com/rw-office-partners

About Page from the website:
My name is Maribel Rowe, and I would love to assist you to become more productive in your day to day and achieve your business and personal goals.
My mission is to give you time, time to work on the important tasks of your business or to be able to spend more time with your family. I will take on the tasks you don’t have time for, don’t know well or simply don’t like to do.
I have an extensive background in Administration, Tender Coordination, Document Control, WHS and Quality Management working primarily in the Construction, Mining and Corporate World.
I am passionate about being organised, having order and making things in your life (and mine) easier! I love to watch something unfold and grow into something amazing! I am known for being the go-to problem solver, the organiser of all things, producing high standards of work even under pressure. I’m also a confident communicator, and I understand that you’re busy running your business.

Target Market(s)

Small to Medium Business who require assistance in their business by a virtual assistant.

Industry/Entity Type

Virtual Assistant

Contact Information for Business Card

Mobile: 61 400 000 000

Font styles to use
Sans Serif

Colors
ffffff

Requirements
Must have
• Branding Colours as outlined.
Contact Details as outlined.
Logo as provided.
Proper contact details - mobile, facebook, instragm, website.
Simple, Elegant, very clean looking.
Should not have
• Note cute with pictures.
Not too girly as still want to market to construction companies.

```html
<!DOCTYPE html>
<html lang="en">
<head>
<meta charset="utf-8">
<title>RW Office Partners – Business Card</title>
<link rel="stylesheet" href="https://fonts.googleapis.com/css2?family=Montserrat:wght@500;600;700&family=Roboto:wght@400;500&display=swap">
<style>
  :root {
    --mauve: #8a5a6e;
    --mauve-light: #ddccd3;
    --slate: #7a8498;
    --slate-light: #c9d8e4;
    --ink: #141216;
    --white: #ffffff;
    --backdrop: #3a3a3c;
  }
  * { margin: 0; padding: 0; box-sizing: border-box; }
  html, body { width: 799px; height: 1200px; overflow: hidden; }
  body {
    background: var(--backdrop);
    font-family: "Roboto", Arial, sans-serif;
    position: relative;
  }
  .card {
    position: absolute;
    left: 80px;
    width: 640px;
    height: 366px;
    background: var(--ink);
    border-radius: 4px;
    overflow: hidden;
    box-shadow: 0 18px 40px rgba(0,0,0,.45);
  }
  .card--front { top: 140px; }
  .card--back { top: 694px; }

  /* Front */
  .front-brand {
    position: absolute;
    left: 0; right: 0; top: 122px;
    text-align: center;
    font-family: "Montserrat", Arial, sans-serif;
    font-weight: 600;
    font-size: 44px;
    letter-spacing: 1px;
    color: var(--slate);
    text-transform: uppercase;
  }
  .front-social {
    position: absolute;
    left: 0; right: 0; top: 258px;
    display: flex;
    justify-content: center;
    gap: 30px;
    color: var(--white);
    font-size: 17px;
  }
  .handle { display: flex; align-items: center; gap: 8px; }
  .handle-mark {
    width: 13px; height: 13px;
    background: var(--mauve);
    border-radius: 2px;
  }

  /* Back */
  .back-shapes { position: absolute; inset: 0; }
  .back-brand {
    position: absolute;
    left: 32px; top: 100px;
    width: 170px;
    font-family: "Montserrat", Arial, sans-serif;
    font-weight: 600;
    font-size: 26px;
    line-height: 1.1;
    color: var(--slate);
    text-transform: uppercase;
  }
  .contact-block {
    position: absolute;
    left: 318px; top: 62px;
    color: var(--white);
  }
  .person-name {
    font-family: "Montserrat", Arial, sans-serif;
    font-weight: 700;
    font-size: 22px;
  }
  .person-role { font-size: 13px; margin-bottom: 12px; }
  .contact-list { list-style: none; font-size: 14.5px; line-height: 21px; }
  .contact-list li { display: flex; align-items: center; gap: 10px; }
  .contact-icon { width: 13px; height: 13px; flex: none; }
  .tagline {
    position: absolute;
    left: 250px; right: 0; top: 298px;
    padding-left: 20px;
    color: var(--white);
    font-size: 16px;
    line-height: 30px;
  }
</style>
</head>
<body>

<section class="card card--front" aria-label="Card front">
  <div class="front-brand">RW Office Partners</div>
  <div class="front-social">
    <span class="handle"><span class="handle-mark"></span>@rwofficepartners</span>
    <span class="handle"><span class="handle-mark"></span>@rwofficepartners</span>
  </div>
</section>

<section class="card card--back" aria-label="Card back">
  <svg class="back-shapes" viewBox="0 0 640 366" width="640" height="366">
    <path d="M284 0 L640 0 L640 366 L146 366 C200 300 246 200 262 100 C266 60 272 30 284 0 Z" fill="var(--slate)"/>
    <path d="M300 0 L640 0 L640 366 L166 366 C218 300 262 200 278 100 C282 60 288 30 300 0 Z" fill="var(--mauve)"/>
    <rect x="200" y="298" width="440" height="30" fill="var(--slate)"/>
  </svg>

  <div class="back-brand">RW Office Partners</div>

  <div class="contact-block">
    <div class="person-name">Maribel Rowe</div>
    <div class="person-role">Virtual Assistant</div>
    <ul class="contact-list">
      <li>
        <svg class="contact-icon" viewBox="0 0 16 16"><path d="M4 1 L6.5 4.5 L5 6 C6 8.5 7.5 10 10 11 L11.5 9.5 L15 12 L13 15 C7 15 1 9 1 3 Z" fill="var(--white)"/></svg>
        61 400 000 000
      </li>
      <li>
        <svg class="contact-icon" viewBox="0 0 16 16"><rect x="1" y="3" width="14" height="10" fill="none" stroke="var(--white)" stroke-width="1.5"/><path d="M1 3 L8 9 L15 3" fill="none" stroke="var(--white)" stroke-width="1.5"/></svg>
        maribel@rwofficepartners-example.com.au
      </li>
      <li>
        <svg class="contact-icon" viewBox="0 0 16 16"><circle cx="8" cy="8" r="6.5" fill="none" stroke="var(--white)" stroke-width="1.4"/><ellipse cx="8" cy="8" rx="3" ry="6.5" fill="none" stroke="var(--white)" stroke-width="1.2"/><line x1="1.5" y1="8" x2="14.5" y2="8" stroke="var(--white)" stroke-width="1.2"/></svg>
        www.rwofficepartners-example.com.au
      </li>
      <li>
        <svg class="contact-icon" viewBox="0 0 16 16"><rect x="2" y="2" width="12" height="12" rx="2" fill="var(--white)"/></svg>
        @rwofficepartners
      </li>
      <li>
        <svg class="contact-icon" viewBox="0 0 16 16"><rect x="2" y="2" width="12" height="12" rx="2" fill="var(--white)"/></svg>
        @rwofficepartners
      </li>
    </ul>
  </div>

  <div class="tagline">Your organised problem solver</div>
</section>

</body>
</html>
```